Short term Rentals Marketing agency needs Web design.

We Need a web design for our new company based in Calgary, AB. We are a International Luxury home sharing company (short term rental properties, Villas, Boutique Hotels, Bed & Breakfast, Realtors, Mortgage Brokers). We would like to see designs that look simple, modern and professional. Colors would be bold (red, black, white). The final design should communicate something welcoming, symbolize innovation, and growth. Our goal is to form partnerships with Real Estate, Property Management, Short term Rental Clients to make their lives easier and increase revenue. Vlto Harbor Co. offers a flexible and secure way to market our clients properties while maintaining client satisfaction and amazing customer service. We like how https://brinkleafpromo.ca/ is interactive (when you scroll down, text gets larger). Other similar websites for Short Term Rentals is https://www.quillnestgroup.com/, https://dwelvaroo.com/, https://www.kipmarsh.com/, https://www.tarnpenny.com/about-us/, https://vantrelstays.com. We have attached our Logo.

Target Market(s)

short term rental properties, Villas, Boutique Hotels, Bed & Breakfast, Realtors, Mortgage Brokers, property owners

Industry/Entity Type

Real Estate

Coding

Coded - Design and coding required

Number of Pages Required

5+ page

Font styles to use
Sans Serif

Requirements
Must have
• Home Page, About Us page, How it works, Services, Contact us.

We like how https://brinkleafpromo.ca/ is interactive (when you scroll down, text gets larger).

We have attached our Webcopy. We would like Call to Action Buttons where they're located in the copy and page.

Must have our Logo Colors.

Other similar websites for Short Term Rentals is https://www.quillnestgroup.com/, https://dwelvaroo.com/, https://www.kipmarsh.com/, https://www.tarnpenny.com/about-us/, https://vantrelstays.com.
Nice to have
• Catchy, Interactive Home page.

Should not have
• Should not be too cluttered

```html
<!DOCTYPE html>
<html lang="en">
<head>
<meta charset="utf-8">
<title>Vlto Harbor Co.</title>
<link href="https://fonts.googleapis.com/css2?family=Roboto:wght@300;400;500;700&display=swap" rel="stylesheet">
<style>
:root{
  --red:#e31b23;
  --ink:#111111;
  --text:#222222;
  --muted:#7a7a7a;
  --tan:#9c7b55;
  --soft:#f6f6f6;
  --white:#ffffff;
  --line:#ececec;
}
*{box-sizing:border-box;margin:0;padding:0}
html,body{width:1200px;height:4334px;overflow:hidden}
body{font-family:"Roboto",Arial,sans-serif;color:var(--text);background:var(--white);position:relative}
section,header,footer{position:absolute;left:0;width:1200px}
.abs{position:absolute}
.label{font-size:12px;font-weight:500;letter-spacing:3px;text-transform:uppercase;color:#555}
.btn{position:absolute;display:flex;align-items:center;justify-content:center;font-size:12px;font-weight:700;letter-spacing:2px;text-transform:uppercase;color:var(--white)}
.btn-red{background:var(--red);box-shadow:0 6px 14px rgba(227,27,35,.25)}
.photo{position:absolute}
.brand{display:flex;align-items:center;gap:14px}
.brand-mark{width:42px;height:42px;background:var(--red)}
.brand-name{font-size:34px;font-weight:300;letter-spacing:.5px}

/* hero */
.hero{top:0;height:638px;background:linear-gradient(100deg,#c9a59a 0%,#a88677 35%,#6b4b38 65%,#4a3226 100%)}
.hero-shade{position:absolute;inset:0;background:rgba(40,25,20,.28)}
.nav{position:absolute;left:21px;top:59px;display:flex;gap:21px;font-size:12px;font-weight:500;color:var(--white)}
.hero .brand{position:absolute;left:512px;top:42px;color:var(--white)}
.contact-item{position:absolute;top:46px;display:flex;gap:14px;color:var(--white)}
.contact-icon{width:24px;height:24px;background:var(--red);border-radius:3px;display:flex;align-items:center;justify-content:center;margin-top:4px}
.contact-item small{display:block;font-size:11px;font-weight:500}
.contact-item span{display:block;font-size:17px;margin-top:6px}
.hero-kicker{position:absolute;top:309px;width:100%;text-align:center;color:var(--white);font-size:12px;font-weight:700;letter-spacing:3px}
.hero-title{position:absolute;top:348px;width:100%;text-align:center;color:var(--white);font-size:44px;font-weight:400;line-height:50px}
.btn-ghost{border:1px solid rgba(255,255,255,.6)}

/* how it works */
.how{top:638px;height:658px}
.plane{left:0;top:300px;width:320px;height:230px;background:linear-gradient(135deg,rgba(0,0,0,.03),rgba(0,0,0,0))}
.how .label{left:103px;top:93px}
.how-title{left:103px;top:126px;font-size:28px;font-weight:400}
.how-text{left:103px;top:180px;width:320px;font-size:16px;line-height:28px;color:var(--tan)}
.btn-dark{background:var(--ink);box-shadow:0 6px 14px rgba(0,0,0,.25)}
.step{position:absolute;left:510px;width:620px;height:110px}
.step-icon{position:absolute;left:0;top:0;width:104px;height:101px;background:var(--white);border-radius:10px;box-shadow:0 8px 22px rgba(0,0,0,.08);display:flex;align-items:center;justify-content:center}
.step h3{position:absolute;left:141px;top:0;font-size:24px;font-weight:400}
.step p{position:absolute;left:141px;top:40px;width:460px;font-size:11.5px;line-height:19px;color:var(--muted)}
.red-bar{left:30px;top:596px;width:1140px;height:15px;background:var(--red)}

/* about */
.about{top:1303px;height:579px;background:linear-gradient(90deg,#f4f1ef,#fbfaf9 40%,#f5f2f0)}
.about .label{left:698px;top:160px}
.about-title{left:698px;top:192px;font-size:29px;font-weight:400}
.about-text{left:698px;top:247px;width:385px;font-size:13px;line-height:22px;color:var(--muted)}

/* features */
.features{top:1882px;height:560px;background:var(--soft)}
.features .label{top:43px;width:100%;text-align:center}
.label .accent{color:var(--red)}
.features-title{top:72px;width:100%;text-align:center;font-size:29px;font-weight:400;line-height:34px}
.feature{position:absolute;width:176px;height:182px;background:var(--white);border-radius:8px;box-shadow:0 6px 20px rgba(0,0,0,.05);display:flex;flex-direction:column;align-items:center;justify-content:center;gap:16px}
.feature span{font-size:11px;font-weight:700;letter-spacing:2.5px}

/* services */
.services{top:2442px;height:899px}
.services .label{top:55px;width:100%;text-align:center}
.services-title{top:90px;width:100%;text-align:center;font-size:29px;font-weight:400}
.service{position:absolute;width:315px;height:313px;border:1px solid var(--line);background:var(--white);overflow:hidden}
.service .num{position:absolute;right:4px;top:-10px;font-size:100px;font-weight:700;color:#f4f4f4}
.service .ico{position:absolute;left:44px;top:44px}
.service h3{position:absolute;left:44px;top:136px;font-size:25px;font-weight:400}
.service p{position:absolute;left:44px;top:196px;width:225px;font-size:11.5px;line-height:19px;color:var(--muted)}

/* testimonials */
.testimonials{top:3341px;height:676px;background:var(--soft)}
.testimonials .label{top:47px;width:100%;text-align:center}
.testimonials-title{top:82px;width:100%;text-align:center;font-size:29px;font-weight:400}
.review{position:absolute;top:180px;width:315px;height:407px;background:var(--white);text-align:center}
.portrait{position:absolute;left:91px;top:42px;width:132px;height:132px;background:linear-gradient(160deg,#6b5a4f,#2f2a28)}
.review h4{position:absolute;top:204px;width:100%;font-size:26px;font-weight:400}
.review .role{position:absolute;top:254px;width:100%;font-size:13px;font-weight:700;letter-spacing:2.5px;color:var(--red)}
.review p{position:absolute;top:293px;left:32px;width:251px;font-size:12.5px;line-height:22px;color:var(--muted)}
.dots{position:absolute;top:616px;left:552px;display:flex;gap:10px}
.dots i{display:block;width:14px;height:3px;background:#ddd}
.dots i.on{width:22px;background:var(--red)}

/* footer */
.footer{top:4017px;height:219px}
.footer .brand{position:absolute;left:486px;top:50px;color:var(--ink)}
.footer .brand-mark{width:62px;height:62px}
.footer .brand-name{font-size:44px}
.footer-text{top:156px;width:100%;text-align:center;font-size:13px;line-height:22px;color:var(--muted)}
.bottom{top:4236px;height:98px;background:var(--ink)}
.copyright{left:96px;top:50px;font-size:12px;font-weight:700;letter-spacing:2px;color:var(--white)}
.social{position:absolute;top:22px;width:54px;height:54px;background:#1f1f1f;display:flex;align-items:center;justify-content:center}
.social i{display:block;width:12px;height:12px;background:var(--white);border-radius:2px}
</style>
</head>
<body>

<header class="hero">
  <div class="photo" role="img" aria-label="Warm bedroom interior with wooden barn door and pink bedding" style="inset:0;background:linear-gradient(100deg,#d5b0a6 0%,#b39280 35%,#6e4c38 65%,#4a3226 100%)"></div>
  <div class="hero-shade"></div>
  <nav class="nav"><span>Home</span><span>About Us</span><span>Our Services</span><span>How It Works</span><span>Contact</span></nav>
  <div class="brand"><div class="brand-mark"></div><div class="brand-name">vlto harbor co.</div></div>
  <div class="contact-item" style="left:827px">
    <div class="contact-icon"><svg width="12" height="10" viewBox="0 0 12 10"><rect x=".5" y=".5" width="11" height="9" fill="none" stroke="#fff"/><path d="M.5 .5 6 5l5.5-4.5" fill="none" stroke="#fff"/></svg></div>
    <div><small>Email Address</small><span>info@example.com</span></div>
  </div>
  <div class="contact-item" style="left:1034px">
    <div class="contact-icon"><svg width="12" height="12" viewBox="0 0 12 12"><path d="M2 1l2 0 1 3-1.5 1a7 7 0 0 0 3.5 3.5L8 7l3 1v2c0 1-1 1-1 1A9 9 0 0 1 1 2s0-1 1-1z" fill="none" stroke="#fff"/></svg></div>
    <div><small>Phone Number</small><span>+123 456 789</span></div>
  </div>
  <div class="hero-kicker">LOREM IPSUM DOLOR SIT AMET</div>
  <h1 class="hero-title">Partner With Us And<br>Let’s Start Growing Together!</h1>
  <div class="btn btn-ghost" style="left:395px;top:475px;width:184px;height:53px">Let’s Start</div>
  <div class="btn btn-red" style="left:604px;top:475px;width:185px;height:53px">Contact Us</div>
</header>

<section class="how">
  <div class="abs plane" role="img" aria-label="Faint paper plane line illustration"></div>
  <div class="abs label">How It Works</div>
  <h2 class="abs how-title">Title Here</h2>
  <p class="abs how-text">Lorem ipsum dolor sit amet, consectetur adipisicing elit. Vel, assumenda.</p>
  <div class="btn btn-dark" style="left:103px;top:270px;width:228px;height:56px">See How It Work</div>

  <div class="step" style="top:94px">
    <div class="step-icon"><svg width="52" height="48" viewBox="0 0 52 48" fill="none" stroke="#e31b23" stroke-width="2"><path d="M4 22 26 4l22 18"/><path d="M10 18v26h32V18"/><rect x="26" y="28" width="12" height="10"/><path d="M32 28v10M26 33h12"/><rect x="15" y="28" width="7" height="16"/><circle cx="26" cy="16" r="3"/></svg></div>
    <h3>Title Here</h3>
    <p>Lorem ipsum dolor sit amet, consectetur adipiscing elit, sed do eiusmod tempor incididunt ut labore et dolore magna aliqua. Ut enim ad minim veniam, quis nostrud exercitation ullamco laboris nisi ut aliquip ex ea commodo consequat.</p>
  </div>
  <div class="step" style="top:239px">
    <div class="step-icon"><svg width="48" height="54" viewBox="0 0 48 54" fill="none" stroke="#e31b23" stroke-width="2"><path d="M24 40S10 26 10 16a14 14 0 0 1 28 0c0 10-14 24-14 24z"/><circle cx="24" cy="16" r="6"/><path d="M16 38 4 48h40L32 38"/></svg></div>
    <h3>Title Here</h3>
    <p>Lorem ipsum dolor sit amet, consectetur adipiscing elit, sed do eiusmod tempor incididunt ut labore et dolore magna aliqua. Ut enim ad minim veniam, quis nostrud exercitation ullamco laboris nisi ut aliquip ex ea commodo consequat.</p>
  </div>
  <div class="step" style="top:384px">
    <div class="step-icon"><svg width="54" height="44" viewBox="0 0 54 44" fill="none" stroke="#e31b23" stroke-width="2"><rect x="8" y="4" width="38" height="18" rx="2"/><rect x="14" y="14" width="10" height="8"/><rect x="30" y="14" width="10" height="8"/><path d="M4 22h46v12H4zM8 34v6M46 34v6"/><path d="M14 9h26" stroke-dasharray="2 3"/></svg></div>
    <h3>Title Here</h3>
    <p>Lorem ipsum dolor sit amet, consectetur adipiscing elit, sed do eiusmod tempor incididunt ut labore et dolore magna aliqua. Ut enim ad minim veniam, quis nostrud exercitation ullamco laboris nisi ut aliquip ex ea commodo consequat.</p>
  </div>
  <div class="abs red-bar"></div>
</section>

<section class="about">
  <div class="photo" role="img" aria-label="Bright sunroom living area with arched windows and tiled floor" style="left:99px;top:87px;width:488px;height:421px;background:linear-gradient(160deg,#e9e4dc 0%,#c8c0b2 45%,#8d7d66 100%)"></div>
  <div class="abs label">About Us</div>
  <h2 class="abs about-title">Lorem ipsum dolor sit amet,</h2>
  <p class="abs about-text">Lorem ipsum dolor sit amet, consectetur adipisicing elit. Doloremque quisquam necessitatibus beatae perferendis laborum, reiciendis mollitia animi optio, sunt, possimus porro! Tempore veniam mollitia ab fugiat aliquam, eligendi nihil dolorem.</p>
  <div class="btn btn-red" style="left:698px;top:388px;width:174px;height:56px">Book Now</div>
</section>

<section class="features">
  <div class="abs label">Heading <span class="accent">Text Here</span></div>
  <h2 class="abs features-title">Lorem ipsum dolor sit amet, consectetur adipisicing elit. Totam cum aliquid<br>commodi molestias incidunt sed?</h2>
  <div class="feature" style="left:99px;top:163px">
    <svg width="64" height="60" viewBox="0 0 52 48" fill="none" stroke="#e31b23" stroke-width="1.8"><path d="M4 22 26 4l22 18"/><path d="M10 18v26h32V18"/><rect x="26" y="28" width="12" height="10"/><path d="M32 28v10M26 33h12"/><rect x="15" y="28" width="7" height="16"/><circle cx="26" cy="16" r="3"/></svg>
    <span>TITLE HERE</span>
  </div>
  <div class="feature" style="left:306px;top:250px">
    <svg width="64" height="52" viewBox="0 0 54 44" fill="none" stroke="#e31b23" stroke-width="1.8"><rect x="8" y="4" width="38" height="18" rx="2"/><rect x="14" y="14" width="10" height="8"/><rect x="30" y="14" width="10" height="8"/><path d="M4 22h46v12H4zM8 34v6M46 34v6"/></svg>
    <span>TITLE HERE</span>
  </div>
  <div class="feature" style="left:512px;top:338px">
    <svg width="60" height="64" viewBox="0 0 48 54" fill="none" stroke="#e31b23" stroke-width="1.8"><path d="M24 40S10 26 10 16a14 14 0 0 1 28 0c0 10-14 24-14 24z"/><path d="M18 18l6-6 6 6v6H18z"/><path d="M16 38 4 48h40L32 38"/></svg>
    <span>TITLE HERE</span>
  </div>
  <div class="feature" style="left:719px;top:250px">
    <svg width="64" height="64" viewBox="0 0 50 50" fill="none" stroke="#e31b23" stroke-width="1.8"><circle cx="25" cy="25" r="22"/><circle cx="25" cy="25" r="17"/><path d="M25 13v12l7 5"/></svg>
    <span>TITLE HERE</span>
  </div>
  <div class="feature" style="left:924px;top:163px">
    <svg width="64" height="60" viewBox="0 0 54 50" fill="none" stroke="#e31b23" stroke-width="1.8"><path d="M6 20 27 4l21 16"/><circle cx="27" cy="14" r="5"/><path d="M25 14l2 2 3-3"/><path d="M8 24h30v10H8zM8 34v6M38 34v6M8 28h30"/><circle cx="45" cy="28" r="3"/><path d="M42 34h6v10"/></svg>
    <span>TITLE HERE</span>
  </div>
</section>

<section class="services">
  <div class="abs label">Our Services</div>
  <h2 class="abs services-title">Lorem ipsum is dolor</h2>
  <div class="service" style="left:99px;top:194px">
    <div class="num">01</div>
    <svg class="ico" width="62" height="60" viewBox="0 0 62 60" fill="none" stroke="#e31b23" stroke-width="1.8"><circle cx="26" cy="26" r="22"/><circle cx="26" cy="26" r="17"/><path d="M26 14v12l7 5"/><circle cx="46" cy="44" r="10" fill="#fff"/><path d="M42 40l8 8M50 40l-8 8"/></svg>
    <h3>Title Here</h3>
    <p>Lorem ipsum dolor sit amet, consectetur adipiscing elit, sed do eiusmod tempor incididunt ut labore et dolore magna..</p>
  </div>
  <div class="photo" role="img" aria-label="Open plan living room with sofa, coffee table and kitchen behind" style="left:443px;top:194px;width:314px;height:313px;background:linear-gradient(170deg,#f1ede6 0%,#cbbfae 50%,#7a6652 100%)"></div>
  <div class="service" style="left:786px;top:194px">
    <div class="num">03</div>
    <svg class="ico" width="60" height="60" viewBox="0 0 60 60" fill="none" stroke="#e31b23" stroke-width="2"><path d="M30 4l6 5 8-1 2 8 7 4-3 7 3 7-7 4-2 8-8-1-6 5-6-5-8 1-2-8-7-4 3-7-3-7 7-4 2-8 8 1z"/><path d="M22 38l16-16"/><circle cx="23" cy="24" r="3"/><circle cx="37" cy="36" r="3"/></svg>
    <h3>Title Here</h3>
    <p>Lorem ipsum dolor sit amet, consectetur adipiscing elit, sed do eiusmod tempor incididunt ut labore et dolore magna..</p>
  </div>
  <div class="photo" role="img" aria-label="Bedroom with pink bedding, ceiling fan and sliding barn door" style="left:99px;top:537px;width:315px;height:313px;background:linear-gradient(170deg,#efe2d2 0%,#d2b59c 55%,#b06e6c 100%)"></div>
  <div class="service" style="left:443px;top:537px">
    <div class="num">05</div>
    <svg class="ico" width="62" height="62" viewBox="0 0 50 50" fill="none" stroke="#e31b23" stroke-width="1.8"><circle cx="25" cy="25" r="22"/><circle cx="25" cy="25" r="17"/><path d="M25 13v12l7 5"/></svg>
    <h3>Title Here</h3>
    <p>Lorem ipsum dolor sit amet, consectetur adipiscing elit, sed do eiusmod tempor incididunt ut labore et dolore magna..</p>
  </div>
  <div class="photo" role="img" aria-label="Living room with beige sofa and wooden coffee table" style="left:786px;top:537px;width:315px;height:313px;background:linear-gradient(170deg,#f0ebe3 0%,#c7baa6 50%,#756048 100%)"></div>
</section>

<section class="testimonials">
  <div class="abs label">Testimonials</div>
  <h2 class="abs testimonials-title">Client Feedback</h2>
  <div class="review" style="left:99px">
    <div class="portrait" role="img" aria-label="Client portrait photo"></div>
    <h4>Johe Doe</h4><div class="role">FOUNDER</div>
    <p>Lorem ipsum dolor sit amet, consectetur adipiscing elit, sed do eiusmod tempor incididunt ut labore et dolore.</p>
  </div>
  <div class="review" style="left:443px">
    <div class="portrait" role="img" aria-label="Client portrait photo"></div>
    <h4>Johe Doe</h4><div class="role">CEO</div>
    <p>Lorem ipsum dolor sit amet, consectetur adipiscing elit, sed do eiusmod tempor incididunt ut labore et dolore.</p>
  </div>
  <div class="review" style="left:786px">
    <div class="portrait" role="img" aria-label="Client portrait photo"></div>
    <h4>Johe Doe</h4><div class="role">FOUNDER</div>
    <p>Lorem ipsum dolor sit amet, consectetur adipiscing elit, sed do eiusmod tempor incididunt ut labore et dolore.</p>
  </div>
  <div class="dots"><i></i><i class="on"></i><i></i><i></i></div>
</section>

<footer class="footer">
  <div class="brand"><div class="brand-mark"></div><div class="brand-name">vlto harbor co.</div></div>
  <p class="abs footer-text">Lorem ipsum dolor sit amet, consectetur adipiscing elit, sed doing eiusmod tempor incididunt ut labore et<br>dolore magna aliqua. Ut enim ad minim veniam, quis nostrud exercitation ullamco laboris nisi.</p>
</footer>
<section class="bottom">
  <div class="abs copyright">COPYRIGHT BY @ VLTO HARBOR</div>
  <div class="social" style="left:850px" aria-label="Social link"><i></i></div>
  <div class="social" style="left:916px" aria-label="Social link"><i></i></div>
  <div class="social" style="left:981px" aria-label="Social link"><i></i></div>
  <div class="social" style="left:1047px" aria-label="Social link"><i></i></div>
</section>

</body>
</html>
```